KRT homes
KRT homes business card/letterhead
Project: KRT homes
KRT homes - Real Estate
Creative Brief
Simple
Gregory Varnell
President
742 Birch Lane Suite 3 Walpole, MA 02047
pvarnell@krtdwellings.example
krtdwellings.example
Also need business cards for Pam Teravin Broker Cell 508.555.0187 Email: pteravin@krtdwellings.example Colleen Teravin Varnell Vice President Cell 508.555.0142 Email: colleen@krtdwellings.example
Maybe large version of logo?

```html
<!DOCTYPE html>
<html lang="en">
<head>
<meta charset="utf-8">
<title>KRT homes stationery</title>
<link href="https://fonts.googleapis.com/css2?family=Arimo:wght@400;700&display=swap" rel="stylesheet">
<style>
  :root {
    --navy: #1b3f8e;
    --blue: #1f56b8;
    --orange: #e8641e;
    --paper: #ffffff;
    --ground: #ffffff;
    --grey: #8a8f99;
    --faint: #eef1f7;
    --edge: #d9dce2;
  }
  * { box-sizing: border-box; margin: 0; padding: 0; }
  html, body { width: 1200px; height: 310px; overflow: hidden; background: var(--ground); font-family: "Arimo", Arial, sans-serif; }
  .canvas { position: relative; width: 1200px; height: 310px; }
  .sheet { position: absolute; background: var(--paper); box-shadow: 0 1px 3px rgba(0,0,0,.28); overflow: hidden; }
  .wordmark { display: flex; align-items: center; gap: 4px; color: var(--navy); font-weight: 700; white-space: nowrap; }
  .wordmark .dot { width: .55em; height: .55em; background: var(--orange); flex: none; }
  .wordmark.light { color: #fff; }

  .brand-block { position: absolute; left: 28px; top: 30px; width: 260px; }
  .brand-block .wordmark { font-size: 36px; }
  .brand-block .tagline { font-size: 9px; color: var(--grey); margin: 4px 0 0 28px; }

  .card { width: 120px; height: 66px; padding: 7px; }
  .card .wordmark { font-size: 10px; }
  .card .name { font-size: 5px; font-weight: 700; color: var(--navy); margin-top: 6px; }
  .card .line { font-size: 4px; color: var(--grey); line-height: 1.4; white-space: nowrap; }
  .card.front { left: 24px; top: 122px; }
  .card.back { left: 150px; top: 122px; }
  .card.logo-white { left: 24px; top: 206px; display: flex; align-items: center; justify-content: center; }
  .card.logo-white .wordmark { font-size: 14px; }
  .card.logo-blue { left: 150px; top: 206px; background: var(--blue); display: flex; align-items: center; justify-content: center; }
  .card.logo-blue .wordmark { font-size: 14px; }

  .letterhead { width: 168px; height: 264px; top: 20px; padding: 12px; border-left: 3px solid var(--blue); }
  .letterhead.first { left: 300px; }
  .letterhead.second { left: 492px; }
  .letterhead .head { display: flex; justify-content: center; }
  .letterhead .head .wordmark { font-size: 11px; }
  .letterhead .faint-name { position: absolute; left: 0; right: 0; top: 110px; text-align: center; font-size: 24px; font-weight: 700; color: var(--faint); white-space: nowrap; }
  .letterhead .foot { position: absolute; left: 0; right: 0; bottom: 10px; text-align: center; font-size: 4px; color: var(--grey); line-height: 1.5; }

  .envelope { width: 176px; height: 52px; left: 700px; padding: 7px; border-left: 3px solid var(--blue); }
  .envelope.upper { top: 118px; }
  .envelope.lower { top: 230px; }
  .envelope .wordmark { font-size: 8px; }
  .envelope .addr { font-size: 4px; color: var(--grey); margin-top: 3px; white-space: nowrap; }
  .envelope .web { position: absolute; left: 0; right: 0; bottom: 4px; text-align: center; font-size: 4px; color: var(--grey); }

  .flap-env { position: absolute; left: 940px; width: 236px; height: 52px; }
  .flap-env svg { display: block; filter: drop-shadow(0 1px 2px rgba(0,0,0,.3)); }
  .flap-env.orange { top: 96px; }
  .flap-env.white-front { top: 162px; }
  .flap-env.white-back { top: 228px; }
</style>
</head>
<body>
<div class="canvas">

  <div class="brand-block">
    <div class="wordmark"><span class="dot"></span>KRT homes</div>
    <div class="tagline">Stationery Concept</div>
  </div>

  <div class="sheet card front">
    <div class="wordmark"><span class="dot"></span>KRT homes</div>
    <div class="name">Gregory Varnell</div>
    <div class="line">President</div>
    <div class="line">742 Birch Lane Suite 3 Walpole, MA 02047</div>
    <div class="line">pvarnell@krtdwellings.example</div>
  </div>
  <div class="sheet card back">
    <div class="wordmark"><span class="dot"></span>KRT homes</div>
    <div class="name">Pam Teravin</div>
    <div class="line">Broker · Cell 508.555.0187</div>
    <div class="line">pteravin@krtdwellings.example</div>
    <div class="line">krtdwellings.example</div>
  </div>
  <div class="sheet card logo-white">
    <div class="wordmark"><span class="dot"></span>KRT homes</div>
  </div>
  <div class="sheet card logo-blue">
    <div class="wordmark light">KRT homes</div>
  </div>

  <div class="sheet letterhead first">
    <div class="head"><div class="wordmark"><span class="dot"></span>KRT homes</div></div>
    <div class="faint-name">KRT homes</div>
    <div class="foot">742 Birch Lane Suite 3 Walpole, MA 02047<br>krtdwellings.example</div>
  </div>
  <div class="sheet letterhead second">
    <div class="head"><div class="wordmark"><span class="dot"></span>KRT homes</div></div>
    <div class="faint-name">KRT homes</div>
    <div class="foot">742 Birch Lane Suite 3 Walpole, MA 02047<br>krtdwellings.example</div>
  </div>

  <div class="sheet envelope upper">
    <div class="wordmark"><span class="dot"></span>KRT homes</div>
    <div class="addr">742 Birch Lane Suite 3 Walpole, MA 02047</div>
    <div class="web">krtdwellings.example</div>
  </div>
  <div class="sheet envelope lower">
    <div class="wordmark"><span class="dot"></span>KRT homes</div>
    <div class="addr">742 Birch Lane Suite 3 Walpole, MA 02047</div>
    <div class="web">krtdwellings.example</div>
  </div>

  <div class="flap-env orange">
    <svg width="236" height="52" viewBox="0 0 236 52">
      <rect x="1" y="1" width="234" height="49" fill="#fff"/>
      <path d="M1 1 H235 V16 L118 30 L1 16 Z" fill="var(--orange)"/>
    </svg>
  </div>
  <div class="flap-env white-front">
    <svg width="236" height="52" viewBox="0 0 236 52">
      <rect x="1" y="1" width="234" height="49" fill="#fff"/>
      <path d="M1 1 L118 28 L235 1" fill="none" stroke="var(--edge)"/>
      <path d="M1 50 L96 24 M235 50 L140 24" fill="none" stroke="var(--edge)"/>
    </svg>
  </div>
  <div class="flap-env white-back">
    <svg width="236" height="52" viewBox="0 0 236 52">
      <rect x="1" y="1" width="234" height="49" fill="#fff"/>
      <path d="M1 1 L118 30 L235 1" fill="none" stroke="var(--edge)"/>
      <path d="M1 50 L104 26 M235 50 L132 26" fill="none" stroke="var(--edge)"/>
    </svg>
  </div>

</div>
</body>
</html>
```